Wedding Invitation : Who helps to design a chic wedding card?

We need a chic invitation design for our wedding invitations.

FRONT

- Name logo : Mirte & Koen
- Wedding date : zaterdag 9 juli 2022
- Quote : forever starts here

BACK

- Wij geven elkaar het ja-woord op zaterdag 9 juli 2022
Translation: We’ll say yes on Saturday 9th of July 2022 in the church of Brambeke
- Timeline with icons:

o JAWOORD (Translation: We say yes)
o 15u00

o RECEPTIE (Translation: Reception)
o 18u30

o DINER (Translation: Dinner)
o 19u30
o Feestzaal Volderhof (Location)

o FEEST (Translation: Dinner)
o 21u30

- Locations:

o Icon of a church:
Brambeke
o Icon of a location:
Feestzaal Volderhof
Kapelmeester Drovenstraat 47B
9870 Oudelinde

- RSVP Gelieve jouw aanwezigheid te bevestigen voor 29 mei 2022
(Translation: Please confirm before 29th of May 2022)

STYLE:

- Rosé gold relief press symbols
- Font style : handwritten or serif name (eg. playfair display)
- Font style: description in a more minimalistic font
- Cards will be in craft or ivory white, text will be in rosé gold relief press or black print

FORMAT
American format (229mm W x 114 mm H)

Target Market(s)

People 25-40 years old

Industry/Entity Type

Wedding / Event

Font styles to use
Serif
Sans Serif
Script

Colors

Designer to choose colors to be used in the design.

Requirements
Must have
• Name logo
Nice to have
• Minimalistic animation / icons
Should not have
• Jungle prints

```html
<!DOCTYPE html>
<html lang="nl">
<head>
<meta charset="utf-8">
<title>Mirte &amp; Koen – Huwelijksuitnodiging</title>
<link rel="stylesheet" href="https://fonts.googleapis.com/css2?family=Dancing+Script:wght@500;600&family=Playfair+Display:ital,wght@0,400;0,600;1,600;1,700&family=Cormorant+Garamond:ital,wght@1,400&display=swap">
<style>
  :root {
    --backdrop: #f08a8a;
    --paper: #f4f3f1;
    --rose-gold: #b8574a;
    --rose-gold-light: #d47a66;
    --rose-gold-dark: #9c4236;
    --serif: "Playfair Display", Georgia, serif;
    --script: "Dancing Script", cursive;
    --slim: "Cormorant Garamond", Georgia, serif;
  }
  * { box-sizing: border-box; margin: 0; padding: 0; }
  html, body { width: 1200px; height: 960px; overflow: hidden; }
  body { background: var(--backdrop); position: relative; font-family: var(--serif); color: var(--rose-gold); }

  .card {
    position: absolute; top: 144px; width: 335px; height: 673px;
    background: var(--paper);
  }
  .card--front { left: 218px; }
  .card--back { left: 636px; }

  .abs { position: absolute; }
  .center { left: 0; right: 0; text-align: center; }

  /* name mark */
  .name-mark {
    position: absolute; border: 1px solid var(--rose-gold); border-radius: 50%;
    display: flex; align-items: center; justify-content: center;
    font-family: var(--serif); font-weight: 600; color: var(--rose-gold);
  }
  .name-mark--front { left: 115px; top: 71px; width: 98px; height: 98px; font-size: 12px; }
  .name-mark--back { left: 132px; top: 544px; width: 66px; height: 66px; font-size: 8.5px; }

  /* front */
  .couple-name {
    font-family: var(--script); font-weight: 600; font-size: 84px; line-height: 1;
    background: linear-gradient(100deg, var(--rose-gold-light), var(--rose-gold-dark) 55%, var(--rose-gold-light));
    -webkit-background-clip: text; background-clip: text; color: transparent;
  }
  .couple-name--first { top: 220px; }
  .couple-name--second { top: 338px; }
  .couple-joiner { top: 316px; font-family: var(--slim); font-style: italic; font-size: 21px; display: flex; justify-content: center; align-items: center; gap: 8px; }
  .couple-joiner::before, .couple-joiner::after { content: ""; width: 18px; border-top: 1px solid var(--rose-gold); }
  .tagline { top: 441px; font-family: var(--slim); font-style: italic; font-size: 16px; }
  .day { top: 518px; font-style: italic; font-weight: 700; font-size: 20px; display: flex; justify-content: center; align-items: center; gap: 10px; }
  .day::before, .day::after { content: ""; width: 26px; border-top: 1px solid var(--rose-gold); }
  .date { top: 556px; font-size: 27px; display: flex; justify-content: center; align-items: center; }
  .date span { padding: 0 9px; line-height: 34px; }
  .date span + span { border-left: 1px solid var(--rose-gold); }

  /* back */
  .intro { top: 42px; font-size: 14.5px; font-weight: 600; line-height: 18px; }
  .timeline-line { left: 161px; width: 1px; background: var(--rose-gold); }
  .timeline-dot {
    width: 50px; height: 50px; border-radius: 50%; left: 136px;
    background: radial-gradient(circle at 35% 30%, var(--rose-gold-light), var(--rose-gold-dark));
  }
  .moment { width: 120px; line-height: 1; }
  .moment--left { right: 210px; text-align: right; }
  .moment--right { left: 196px; }
  .moment-title { font-style: italic; font-weight: 700; font-size: 12.5px; }
  .moment-time { font-size: 18px; margin-top: 2px; }
  .moment-place { font-size: 7.5px; margin-top: 4px; white-space: nowrap; }

  .church { left: 42px; top: 463px; width: 50px; height: 45px; background: linear-gradient(var(--rose-gold-light), var(--rose-gold)); opacity: .35; }
  .church-name { left: 22px; width: 90px; top: 510px; text-align: center; font-weight: 600; font-size: 11.5px; }
  .venue-divider { left: 112px; top: 464px; height: 56px; width: 1px; background: var(--rose-gold); }
  .venue-pin { left: 125px; top: 481px; }
  .venue { left: 160px; top: 476px; line-height: 1.15; }
  .venue-name { font-weight: 600; font-size: 12px; }
  .venue-line { font-size: 8.5px; }

  .rsvp { left: 47px; width: 242px; top: 626px; border-top: 1px solid var(--rose-gold); border-bottom: 1px solid var(--rose-gold); padding: 3px 0; text-align: center; font-size: 7.5px; white-space: nowrap; }
</style>
</head>
<body>

<section class="card card--front" aria-label="Voorkant uitnodiging">
  <div class="name-mark name-mark--front">Mirte &amp; Koen</div>
  <div class="abs center couple-name couple-name--first">Mirte</div>
  <div class="abs center couple-joiner">and</div>
  <div class="abs center couple-name couple-name--second">Koen</div>
  <div class="abs center tagline">forever starts here...</div>
  <div class="abs center day">Zaterdag</div>
  <div class="abs center date"><span>09</span><span>Juli</span><span>22</span></div>
</section>

<section class="card card--back" aria-label="Achterkant uitnodiging">
  <p class="abs center intro">Wij geven elkaar het ja-woord op<br>zaterdag 9 juli 2022</p>

  <div class="abs timeline-line" style="top:164px;height:34px"></div>
  <div class="abs timeline-line" style="top:259px;height:34px"></div>
  <div class="abs timeline-line" style="top:354px;height:34px"></div>

  <div class="abs timeline-dot" style="top:108px" role="img" aria-label="Icoon jawoord"></div>
  <div class="abs timeline-dot" style="top:203px" role="img" aria-label="Icoon receptie"></div>
  <div class="abs timeline-dot" style="top:299px" role="img" aria-label="Icoon diner"></div>
  <div class="abs timeline-dot" style="top:393px" role="img" aria-label="Icoon feest"></div>

  <div class="abs moment moment--left" style="top:122px"><div class="moment-title">Jawoord</div><div class="moment-time">15:00</div></div>
  <div class="abs moment moment--right" style="top:217px"><div class="moment-title">Receptie</div><div class="moment-time">18:30</div></div>
  <div class="abs moment moment--left" style="top:308px"><div class="moment-title">Diner</div><div class="moment-time">19:30</div><div class="moment-place">Feestzaal Volderhof</div></div>
  <div class="abs moment moment--right" style="top:402px"><div class="moment-title">Feest</div><div class="moment-time">21:30</div><div class="moment-place">Feestzaal Volderhof</div></div>

  <div class="abs church" role="img" aria-label="Kerkje van Brambeke"></div>
  <div class="abs church-name">Brambeke</div>
  <div class="abs venue-divider"></div>
  <svg class="abs venue-pin" width="28" height="28" viewBox="0 0 28 28" aria-hidden="true">
    <circle cx="14" cy="14" r="14" fill="#b8574a"/>
    <path d="M14 7.5a4.5 4.5 0 0 0-4.5 4.5c0 3.4 4.5 8.5 4.5 8.5s4.5-5.1 4.5-8.5A4.5 4.5 0 0 0 14 7.5z" fill="none" stroke="#f4f3f1" stroke-width="1"/>
    <circle cx="14" cy="12" r="1.6" fill="none" stroke="#f4f3f1" stroke-width="1"/>
  </svg>
  <div class="abs venue">
    <div class="venue-name">Feestzaal Volderhof</div>
    <div class="venue-line">Kapelmeester Drovenstraat 47B</div>
    <div class="venue-line">9870 Oudelinde</div>
  </div>

  <div class="name-mark name-mark--back">Mirte &amp; Koen</div>

  <p class="abs rsvp">- RSVP Gelieve jouw aanwezigheid te bevestigen voor 29 mei 2022</p>
</section>

</body>
</html>
```